Statement on the current financial and economic crisis, with a focus on Greece,

Anybody can become angry - that is easy, but to be angry with the right person and to the right degree and at the right time and for the right purpose, and in the right way - that is not within everybody's power and is not easy.
(Thessidor ) greek philosopher

i want to do a poster with this words from Thessidor greek philosopher and to show this statement for the greek people... its about for my project that i am doing.
Updates

Target Market(s)

my audience will be greek people but not only, from 18-80 years old for that reason i want my statement to be in english.

Industry/Entity Type

Financial

Requirements
Must have
• Anybody can become angry - that is easy, but to be angry with the right person and to the right degree and at the right time and for the right purpose, and in the right way - that is not within everybody's power and is not easy.
i want to show in my poster this statement from:
Thessidor greek philosopher (384 – 322 BC)

```html
<!DOCTYPE html>
<html lang="en">
<head>
<meta charset="UTF-8">
<title>Anger in the Right Way — Thessidor</title>
<link rel="stylesheet" href="https://fonts.googleapis.com/css2?family=Cinzel:wght@500;700&display=swap">
<style>
  :root {
    --paper: #ffffff;
    --quote-green: #5b8a50;
    --accent-red: #e0221d;
    --attribution: #4f6f47;
    --skin-light: #d9b9a4;
    --skin-mid: #b88f78;
    --shard-green: #7fa287;
    --shard-dark: #2f3a33;
  }
  * { margin: 0; padding: 0; box-sizing: border-box; }
  html, body {
    width: 1200px;
    height: 934px;
    overflow: hidden;
    background: var(--paper);
  }
  .poster {
    position: relative;
    width: 1200px;
    height: 934px;
    background: var(--paper);
    font-family: "Cinzel", "Times New Roman", serif;
  }
  .poster__visual {
    position: absolute;
    left: 470px;
    top: 30px;
    width: 730px;
    height: 904px;
    background:
      radial-gradient(ellipse 38% 26% at 30% 45%, var(--skin-light) 0%, var(--skin-mid) 55%, rgba(184,143,120,0) 100%),
      radial-gradient(ellipse 30% 60% at 92% 55%, var(--shard-green) 0%, rgba(127,162,135,0.55) 55%, rgba(127,162,135,0) 100%),
      radial-gradient(ellipse 50% 35% at 70% 50%, rgba(127,162,135,0.45) 0%, rgba(127,162,135,0) 100%),
      radial-gradient(ellipse 20% 30% at 88% 20%, rgba(47,58,51,0.35) 0%, rgba(47,58,51,0) 100%);
  }
  .quote {
    position: absolute;
    left: 76px;
    top: 108px;
    color: var(--quote-green);
    font-weight: 700;
    font-size: 35px;
    line-height: 43.6px;
    letter-spacing: 0.5px;
    z-index: 1;
  }
  .quote__line { display: block; white-space: nowrap; }
  .quote__key { color: var(--accent-red); }
  .divider {
    position: absolute;
    left: 0;
    top: 792px;
    width: 480px;
    height: 2px;
    background: var(--accent-red);
  }
  .attribution {
    position: absolute;
    left: 0;
    top: 802px;
    width: 480px;
    text-align: center;
    color: var(--attribution);
    font-weight: 500;
    font-size: 18px;
    line-height: 24px;
  }
</style>
</head>
<body>
  <main class="poster">
    <div class="poster__visual" role="img" aria-label="Photograph of a clenched fist punching through shattering green glass shards"></div>

    <p class="quote">
      <span class="quote__line">Anybody can</span>
      <span class="quote__line">become angry -</span>
      <span class="quote__line">that is easy,</span>
      <span class="quote__line">But to be angry</span>
      <span class="quote__line">with the <span class="quote__key">right</span></span>
      <span class="quote__line"><span class="quote__key">person</span> and</span>
      <span class="quote__line">To the <span class="quote__key">right</span></span>
      <span class="quote__line"><span class="quote__key">degree</span> And</span>
      <span class="quote__line">at the <span class="quote__key">right time</span></span>
      <span class="quote__line">and for the <span class="quote__key">right</span></span>
      <span class="quote__line"><span class="quote__key">Purpose</span>, And</span>
      <span class="quote__line">in the <span class="quote__key">right way</span> -</span>
      <span class="quote__line">That is not within</span>
      <span class="quote__line">Everybody's power</span>
      <span class="quote__line">And is not easy.</span>
    </p>

    <div class="divider"></div>

    <p class="attribution">
      Thessidor greek philosopher<br>
      (384 – 322 BC)
    </p>
  </main>
</body>
</html>
```